Label or packaging Design for Hair Care Line

Dear Designer,
We are Corvella, a brand known for our premium hairstyling tools, and we are excited to expand into hair care. We are currently looking for a talented designer to create the label designs for our entire luxury hair care line.
This project is crucial in establishing our visual identity in the hair care market, and we aim to position ourselves alongside premium brands such as LTP, Dorvane Hair Atelier, and Pelmi.
Project Scope
We need a cohesive label design for our hair care line, which includes:
5 products (e.g., shampoo, conditioner, hair oil, styling cream, and a hair mask).
The designs should include:
Front label: Highlighting the product name, key features, and branding.
Our goal is to achieve a design that communicates premium luxury with a touch of professionalism. Below are the specific guidelines to help you align with our vision:
Style and Inspiration
Think of brands like LTP, Dorvane Hair Atelier, and Pelmi.
Luxury and Minimalism: Clean lines, sophisticated typography, and an elegant color palette.
Subtle femininity: premium finishes like metallic accents (gold, silver, or rose gold).
Brand Personality
Premium: Reflecting high quality and exclusivity.
Modern & Professional: Appealing to a refined, professional audience but also suitable for lifestyle-oriented customers.
Warm & Empowering: A brand that celebrates confidence and individuality.
Color Palette
Neutral tones like black, white, accented with metallics (gold or silver) for a luxurious feel.
Colors that feel timeless and elegant rather than trendy or overly bright.
Typography
Use clean, modern fonts (preferably sans-serif or serif for a refined look).
Clear and legible for all product details while maintaining a high-end aesthetic.
Materials and Finishes
Packaging Shape
The label designs should suit a variety of bottle and jar shapes (e.g., cylindrical, flat, or rounded).
Keep scalability in mind so the identity remains consistent across different products.
Deliverables
To understand the aesthetic we are aiming for, here are some brands to use as inspiration:
LTP: For its minimalistic and modern approach.
Dorvane Hair Atelier: For its combination of luxury and professional appeal.
Pelmi: For its soft femininity and lifestyle branding.
we would like to see your designs applied to a variety of packaging types to get an overall impression of how the brand identity works across different product formats. This includes:
A squeeze bottle (e.g., for styling creams or conditioners).
A glass bottle with a dropper (e.g., for a luxurious hair oil).
A shampoo/conditioner bottle (standard pump or flip-top cap).
A spray bottle (e.g., for leave-in treatments or heat protectors).
By creating designs for these different packaging types, we can better evaluate how cohesive and versatile the brand identity will be across the entire product line.

Updates
As you may have noticed from the designs, they don’t quite align with our briefing. The look needs to be clean and professional, similar to Dorvane, LTP, and the other examples we provided. Please address this, and we’ll check it!

Target Market(s)
europe and us
Font styles to use
Other font styles liked:
- century gothic

Look and feel
Each slider illustrates characteristics of the customer's brand and the style your logo design should communicate.

```html
<!DOCTYPE html>
<html lang="en">
<head>
<meta charset="utf-8">
<title>Corvella — Hair Care Label Line</title>
<link rel="stylesheet" href="https://fonts.googleapis.com/css2?family=Montserrat:wght@400;600&display=swap">
<style>
  :root {
    --navy: #272a38;
    --gold: #dcbc90;
    --gold-deep: #c9a877;
    --sky: #98b4d4;
    --paper: #ffffff;
    --shade: #4e5f78;
  }
  * { box-sizing: border-box; margin: 0; padding: 0; }
  html, body { width: 1200px; height: 2498px; overflow: hidden; background: var(--paper); }
  body { font-family: "Montserrat", sans-serif; position: relative; }

  .board {
    position: absolute; left: 0; top: 0; width: 1200px; height: 1511px;
    background: var(--sky);
  }
  .board__shadow { position: absolute; left: 0; top: 1511px; width: 1200px; height: 26px; }

  .label {
    position: absolute; background: var(--navy); overflow: visible;
  }
  .label__pattern {
    position: absolute; left: 0; top: 0; width: 100%; height: var(--split);
    background: linear-gradient(160deg, #2d3142 0%, #3a3a44 45%, #2a2d3b 100%);
  }
  .label__rule {
    position: absolute; left: 0; width: 100%; top: var(--split); height: 5px; background: var(--gold);
  }
  .label__badge {
    position: absolute; left: 50%; top: var(--split);
    width: var(--bw); height: var(--bh);
    transform: translate(-50%, -50%);
    background: var(--navy); border: 2px solid var(--gold); padding: 5px;
  }
  .label__badge-inner {
    width: 100%; height: 100%; background: var(--gold);
    display: flex; align-items: center; justify-content: center;
    color: var(--navy); font-weight: 400; font-size: var(--bf); letter-spacing: 0.01em;
  }
  .label__name {
    position: absolute; left: 0; width: 100%; top: var(--name-y);
    transform: translateY(-50%);
    text-align: center; color: var(--gold); font-weight: 600; font-size: 21px; letter-spacing: 0.03em;
  }
  .label__copy {
    position: absolute; left: 50%; top: var(--copy-y); width: 205px;
    transform: translate(-50%, -50%);
    text-align: center; color: var(--gold); font-size: 5.4px; line-height: 8px;
  }
  .label__base {
    position: absolute; left: 0; width: 100%; top: var(--base-y); height: 6px; background: var(--gold);
  }
  .label__shadow {
    position: absolute; left: 2%; width: 96%; top: 100%; height: 24px;
  }

  .label--shampoo     { left: 65px;  top: 47px;  width: 475px;  height: 475px; --split: 235px; --bw: 144px; --bh: 87px; --bf: 21px; --name-y: 333px; --copy-y: 419px; --base-y: 450px; }
  .label--conditioner { left: 592px; top: 52px;  width: 543px;  height: 470px; --split: 235px; --bw: 144px; --bh: 87px; --bf: 21px; --name-y: 331px; --copy-y: 413px; --base-y: 446px; }
  .label--mask        { left: 65px;  top: 576px; width: 1070px; height: 358px; --split: 177px; --bw: 163px; --bh: 100px; --bf: 24px; --name-y: 293px; --base-y: 352px; }
  .label--styling     { left: 65px;  top: 998px; width: 511px;  height: 443px; --split: 221px; --bw: 134px; --bh: 81px; --bf: 20px; --name-y: 311px; --copy-y: 391px; --base-y: 420px; }
  .label--oil         { left: 623px; top: 998px; width: 512px;  height: 443px; --split: 221px; --bw: 134px; --bh: 81px; --bf: 20px; --name-y: 311px; --copy-y: 391px; --base-y: 420px; }
</style>
</head>
<body>
<svg width="0" height="0" style="position:absolute">
  <defs>
    <linearGradient id="shade-fade" x1="0" x2="1" y1="0" y2="0">
      <stop offset="0" stop-color="#4e5f78" stop-opacity="0.9"/>
      <stop offset="0.5" stop-color="#4e5f78" stop-opacity="0.15"/>
      <stop offset="1" stop-color="#4e5f78" stop-opacity="0.9"/>
    </linearGradient>
  </defs>
</svg>

<main class="board">

  <section class="label label--shampoo">
    <div class="label__pattern" role="img" aria-label="Gold line art deco pattern of interlocking arches"></div>
    <div class="label__rule"></div>
    <div class="label__badge"><div class="label__badge-inner">corvella</div></div>
    <h2 class="label__name">SHAMPOO</h2>
    <p class="label__copy">Gentle daily cleanser with argan oil and silk proteins that lifts away buildup, restores softness and leaves every strand light, glossy and full of life.</p>
    <div class="label__base"></div>
    <svg class="label__shadow" viewBox="0 0 100 10" preserveAspectRatio="none"><path d="M0 0 H100 L100 10 Q50 -2 0 10 Z" fill="url(#shade-fade)"/></svg>
  </section>

  <section class="label label--conditioner">
    <div class="label__pattern" role="img" aria-label="Gold line pattern of overlapping scalloped arches"></div>
    <div class="label__rule"></div>
    <div class="label__badge"><div class="label__badge-inner">corvella</div></div>
    <h2 class="label__name">CONDITIONER</h2>
    <p class="label__copy">Rich detangling conditioner with keratin and shea butter that smooths the cuticle, tames frizz and seals in moisture for soft, manageable hair every day.</p>
    <div class="label__base"></div>
    <svg class="label__shadow" viewBox="0 0 100 10" preserveAspectRatio="none"><path d="M0 0 H100 L100 10 Q50 -2 0 10 Z" fill="url(#shade-fade)"/></svg>
  </section>

  <section class="label label--mask">
    <div class="label__pattern" role="img" aria-label="Gold line art deco pattern of pointed arches and lattice"></div>
    <div class="label__rule"></div>
    <div class="label__badge"><div class="label__badge-inner">corvella</div></div>
    <h2 class="label__name">HAIR MASK</h2>
    <div class="label__base"></div>
    <svg class="label__shadow" viewBox="0 0 100 10" preserveAspectRatio="none"><path d="M0 0 H100 L100 10 Q50 -2 0 10 Z" fill="url(#shade-fade)"/></svg>
  </section>

  <section class="label label--styling">
    <div class="label__pattern" role="img" aria-label="Flowing gold line waves sweeping across the top"></div>
    <div class="label__rule"></div>
    <div class="label__badge"><div class="label__badge-inner">corvella</div></div>
    <h2 class="label__name">STYLING CREAM</h2>
    <p class="label__copy">Light styling cream with flexible hold that defines shape, controls flyaways and protects against heat up to 230°C without weighing hair down.</p>
    <div class="label__base"></div>
    <svg class="label__shadow" viewBox="0 0 100 10" preserveAspectRatio="none"><path d="M0 0 H100 L100 10 Q50 -2 0 10 Z" fill="url(#shade-fade)"/></svg>
  </section>

  <section class="label label--oil">
    <div class="label__pattern" role="img" aria-label="Gold line botanical pattern of leaves and blossoms"></div>
    <div class="label__rule"></div>
    <div class="label__badge"><div class="label__badge-inner">corvella</div></div>
    <h2 class="label__name">HAIR OIL</h2>
    <p class="label__copy">Nourishing hair oil with camellia and jojoba that melts into lengths, seals split ends and adds a weightless, mirror-like shine to every style.</p>
    <div class="label__base"></div>
    <svg class="label__shadow" viewBox="0 0 100 10" preserveAspectRatio="none"><path d="M0 0 H100 L100 10 Q50 -2 0 10 Z" fill="url(#shade-fade)"/></svg>
  </section>

</main>

<svg class="board__shadow" viewBox="0 0 100 10" preserveAspectRatio="none"><path d="M0 0 H100 L100 10 Q50 -3 0 10 Z" fill="url(#shade-fade)" opacity="0.7"/></svg>
</body>
</html>
```